Bluecrest Automotive Service Website Design

We are working with Bluecrest Automotive Service. They are a local mechanic/garage and in need of a new website design.

Some sites to use for inspiration:

https://www.torvalcar.example
https://www.quenbo.example
https://pavels-carcare.example
https://www.ashgrovetotalautocare.example/

Thank you for taking the time to consider designing a website for us. We are web developers based in Stockton, CA, USA. Most of our projects go through the same process. Understanding this process may help you win a project with us. We custom-code all of our websites in-house. We don’t have any requirements as to what tools you use for your design, but we prefer Figma files. For any design that we label as four-stars, we send it to the client for review. The client picks the final design they want us to use. Once we complete this process, we will continue to show additional clients all the four-star sites and purchase them later. Your designs will have multiple chances to sell. For better chances of success, we ask that you follow these guidelines.

IMAGES:
If you use any images or icons in the design, we ask that you have a link to the asset so we can purchase the image/icon. Most of the designs we submit do not have the customer’s images on them unless they have some great images. Be creative; show us the feeling you are trying to portray with your image choices. Use any royalty-free site you choose. We subscribe to Adobe and mainly use their images, but we can purchase images outside of Adobe.

PLEASE NOTE: we will not submit designs to clients with watermarks on the images.

FONTS:
We ask that you identify the fonts used in the design. This can be done in a message if you want. We typically use Google Fonts and Adobe Fonts.

CONTENT:
We're always open to different content and ideas. We often submit designs with stock images so the client can see our vision. We typically take pictures after the website launch to use their images with our vision. Lorem Ipsum is fine for paragraphs, but we ask that you write the headers in correct English. We want to be able to show the vision and identify the sections of the website.

INSPIRATION:
We typically add a couple of links in the brief of websites we like to help you get started in your design.

REVISIONS:
We do not often ask for revisions of the designs unless we see something in the design that may not appeal to the client. If there are slight changes that we want to make, we do that in the development process.

FEEDBACK:
We rarely give feedback on designs during the design process. We are working on many website projects and do not have the time to provide feedback. We usually respond if your request is well thought out and asks specific questions, but a note asking “feedback, please” usually goes unanswered.

```html
<!DOCTYPE html>
<html lang="en">
<head>
<meta charset="utf-8">
<title>Bluecrest Automotive Service</title>
<link href="https://fonts.googleapis.com/css2?family=Lato:wght@400;700;900&display=swap" rel="stylesheet">
<style>
:root{
  --red:#c8141e;
  --red-dark:#9e0f17;
  --ink:#1c1c1c;
  --dark:#202020;
  --footer:#242424;
  --grey:#6b6b6b;
  --light:#f4f4f4;
  --line:#d9d9d9;
  --white:#ffffff;
}
*{box-sizing:border-box;margin:0;padding:0}
html,body{width:1200px;height:4752px;overflow:hidden}
body{font-family:'Lato',sans-serif;color:var(--ink);background:var(--white);position:relative}
section,header,footer{position:absolute;left:0;width:1200px;overflow:hidden}
.abs{position:absolute}
.btn{position:absolute;display:flex;align-items:center;justify-content:center;background:var(--red);color:var(--white);font-size:13px;font-weight:700;letter-spacing:.5px;text-transform:uppercase}
.photo{position:absolute}

/* hero */
.hero{top:0;height:540px;background:#2a2a2a}
.hero .photo{inset:0;background:linear-gradient(90deg,#1a1a1a 0%,#3b3b3b 45%,#5a5a5a 70%,#2b2b2b 100%)}
.hero .shade{position:absolute;inset:0;background:linear-gradient(90deg,rgba(0,0,0,.55),rgba(0,0,0,.1))}
.brand{left:40px;top:22px;color:var(--white);font-weight:900;font-size:30px;letter-spacing:1px}
.top-phone{left:600px;top:14px;color:var(--white);font-size:17px;font-weight:700;display:flex;align-items:center;gap:10px}
.signup{left:900px;top:0;width:260px;height:52px;font-size:18px;text-transform:none}
.nav{left:560px;top:68px;display:flex;gap:44px;color:var(--white);font-size:12px;font-weight:700}
.nav span.active{border-bottom:2px solid var(--red);padding-bottom:4px}
.hero .kicker{left:64px;top:168px;color:var(--white);font-size:18px;letter-spacing:1px}
.hero h1{position:absolute;left:64px;top:196px;color:var(--white);font-size:50px;font-weight:900;line-height:1.1;width:560px}
.hero p{position:absolute;left:64px;top:318px;color:#e6e6e6;font-size:15px;line-height:1.5;width:560px}
.hero .btn{left:64px;top:364px;width:150px;height:38px}

/* drop-off */
.dropoff{top:540px;height:200px;background:var(--dark);color:var(--white)}
.dropoff h2{position:absolute;left:64px;top:62px;font-size:34px;font-weight:400;line-height:1.25}
.dropoff h2 span{display:block;padding-left:80px}
.dropoff p{position:absolute;left:290px;top:70px;width:240px;font-size:14px;line-height:1.45;text-align:center}
.dropoff .photo{left:560px;top:20px;width:360px;height:160px;background:radial-gradient(ellipse at center,#5a5a5a 0%,#2a2a2a 70%)}
.dropoff .btn{left:980px;top:84px;width:140px;height:36px}

/* about */
.about{top:740px;height:530px;background:var(--white)}
.about h2{position:absolute;left:64px;top:80px;font-size:36px;font-weight:400}
.about p{position:absolute;left:64px;top:138px;width:420px;font-size:15px;line-height:1.55;color:var(--grey)}
.about .btn{left:64px;top:382px;width:160px;height:38px}
.about .red-plate{left:680px;top:290px;width:520px;height:120px;background:var(--red);clip-path:polygon(12% 0,100% 0,100% 100%,0 100%)}
.about .photo{left:800px;top:120px;width:220px;height:300px;background:linear-gradient(180deg,#d8d8d8,#9b9b9b);border-radius:4px}

/* lease */
.lease{top:1270px;height:320px;background:#2e2e2e;color:var(--white);text-align:center}
.lease .photo{inset:0;background:linear-gradient(180deg,#3b3b3b,#1f1f1f)}
.lease h2{position:absolute;left:0;width:1200px;top:78px;font-size:36px;font-weight:700}
.lease p{position:absolute;left:0;width:1200px;top:132px;font-size:26px;font-weight:700;line-height:1.35}
.lease .btn{left:530px;top:222px;width:140px;height:36px}

/* services */
.services{top:1590px;height:810px;background:var(--white);text-align:center}
.services h2{position:absolute;left:0;width:1200px;top:62px;font-size:36px;font-weight:400}
.services .sub{position:absolute;left:380px;width:440px;top:114px;font-size:15px;line-height:1.5;color:var(--grey)}
.svc{position:absolute;width:180px;text-align:center;font-size:15px;color:#333}
.svc .ic{width:80px;height:80px;border-radius:50%;background:var(--white);box-shadow:0 2px 12px rgba(0,0,0,.15);margin:0 auto 10px;display:flex;align-items:center;justify-content:center}
.hub{position:absolute;left:410px;top:630px;width:380px;height:190px;background:var(--red);border-radius:190px 190px 0 0;color:var(--white)}
.hub h3{position:absolute;top:80px;width:100%;font-size:18px;font-weight:700}
.hub p{position:absolute;top:108px;left:70px;width:240px;font-size:13px;line-height:1.45}
.hub .badge{position:absolute;left:165px;top:20px;width:50px;height:50px;border-radius:50%;background:var(--white);color:var(--red);font-size:12px;font-weight:900;display:flex;align-items:center;justify-content:center}

/* pro */
.pro{top:2400px;height:590px;background:#0c0c0c;color:var(--white)}
.pro .photo{left:0;top:40px;width:640px;height:520px;background:radial-gradient(ellipse at 45% 55%,#e8e8e8 0%,#8f8f8f 35%,#1a1a1a 70%)}
.pro .floor{left:0;top:540px;width:1200px;height:50px;background:linear-gradient(90deg,#1a1a1a,var(--red-dark) 60%,var(--red))}
.pro .tag{left:740px;top:180px;font-size:40px;font-weight:900;color:var(--red)}
.pro .big{left:790px;top:212px;font-size:128px;font-weight:900;line-height:1;color:var(--white)}
.pro .big2{left:800px;top:330px;font-size:48px;font-weight:900;color:var(--red)}
.pro .town{left:840px;top:394px;font-size:24px;color:var(--white)}
.pro p{position:absolute;left:740px;top:440px;width:370px;font-size:11px;line-height:1.5;color:#bdbdbd;text-align:center}
.pro .btn{left:830px;top:486px;width:120px;height:32px}

/* testimonials */
.testimonials{top:2990px;height:490px;background:var(--white)}
.testimonials h2{position:absolute;left:0;width:1200px;top:98px;text-align:center;font-size:36px;font-weight:400}
.quote{position:absolute;top:180px;width:340px;height:120px;background:var(--light);padding:18px 22px;font-size:12px;line-height:1.55;color:#9a9a9a}
.person{position:absolute;top:348px;display:flex;align-items:center;gap:14px;font-size:13px;color:var(--red);font-weight:700}
.person .avatar{width:50px;height:50px;border-radius:50%;background:linear-gradient(135deg,#d9c3a9,#8c6f55)}
.arrows{position:absolute;left:560px;top:440px;display:flex;gap:24px}

/* contact */
.contact{top:3480px;height:730px;background:var(--white)}
.contact h2{position:absolute;left:0;width:1200px;top:36px;text-align:center;font-size:36px;font-weight:400}
.contact .car{left:60px;top:120px;width:560px;height:270px;background:radial-gradient(ellipse at center,#e0242b 0%,#a10f16 55%,rgba(255,255,255,0) 72%)}
.info{position:absolute;left:800px;display:flex;gap:18px;font-size:16px;color:#333;line-height:1.4}
.info svg{flex:none;margin-top:2px}
.social{position:absolute;left:810px;top:330px;display:flex;gap:14px}
.social span{width:28px;height:28px;border-radius:50%;border:2px solid var(--red)}
.contact .map{left:0;top:400px;width:1200px;height:330px;background:linear-gradient(135deg,#f0efe9 0%,#e6e4dc 55%,#c9dbe6 80%,#b7cfe0 100%)}

/* cta */
.cta{top:4210px;height:90px;background:var(--red);color:var(--white)}
.cta p{position:absolute;left:64px;top:30px;font-size:22px;font-weight:700}
.cta .btn{left:940px;top:28px;width:180px;height:34px;background:var(--white);color:var(--ink);font-size:12px}

/* footer */
.footer{top:4300px;height:452px;background:var(--footer);color:#d5d5d5}
.col{position:absolute;top:50px}
.col h4{font-size:24px;font-weight:400;color:var(--white);margin-bottom:20px}
.col p{font-size:13px;line-height:1.55;width:300px}
.col ul{list-style:none;font-size:13px;line-height:2.4}
</style>
</head>
<body>

<header class="hero">
  <div class="photo" role="img" aria-label="Mechanic working under the open bonnet of a car in a workshop"></div>
  <div class="shade"></div>
  <div class="abs brand">BLUECREST</div>
  <div class="abs top-phone">
    <svg width="18" height="18" viewBox="0 0 24 24" fill="#fff"><path d="M6.6 10.8a15 15 0 006.6 6.6l2.2-2.2a1 1 0 011-.25 11.4 11.4 0 003.6.57 1 1 0 011 1V20a1 1 0 01-1 1A17 17 0 013 4a1 1 0 011-1h3.5a1 1 0 011 1c0 1.25.2 2.45.57 3.57a1 1 0 01-.25 1z"/></svg>
    (555) 014-3239
  </div>
  <div class="btn signup">Sign Up Now</div>
  <nav class="abs nav"><span class="active">HOME</span><span>ABOUT US</span><span>LOCATION</span><span>SERVICES</span><span>CONTACT US</span></nav>
  <div class="abs kicker">WELCOME TO BLUECREST</div>
  <h1>Providing Automotive Repair Services</h1>
  <p>Wayfarer is one of the largest suppliers of auto-related, supplemental products since 1962, servicing over fifteen million customers annually.</p>
  <div class="btn">Find out how</div>
</header>

<section class="dropoff">
  <h2>After Hours <span>Drop-OFF</span></h2>
  <p>We realize that you lead a busy life, so we've made it easy for you to drop off your vehicle 24/7.</p>
  <div class="photo" role="img" aria-label="Car key with remote fob"></div>
  <div class="btn">Book now</div>
</section>

<section class="about">
  <h2>About Us</h2>
  <p>Wayfarer is one of the largest suppliers of auto-related, supplemental products since 1962, servicing over fifteen million customers annually. Our dedication to excellence is one reason we have the pleasure of working with so many roadside members and providing them with coverage they can trust.</p>
  <div class="btn">Read more</div>
  <div class="abs red-plate"></div>
  <div class="photo" role="img" aria-label="Smiling mechanic in red overalls with arms crossed"></div>
</section>

<section class="lease">
  <div class="photo" role="img" aria-label="Dimmed garage interior"></div>
  <h2>Own A Lease?</h2>
  <p>Find out how a Bluecrest Membership Plan<br>can save you hundreds of dollars when you turn in your car.</p>
  <div class="btn">Read more</div>
</section>

<section class="services">
  <h2>Tires, Oil Changes and Auto Repair Services</h2>
  <p class="sub">Wayfarer is one of the largest suppliers of auto-related, supplemental products since 1962, servicing over fifteen million customers annually.</p>
  <svg class="abs" style="left:150px;top:220px" width="900" height="600" viewBox="0 0 900 600">
    <path d="M20 590 A430 430 0 0 1 880 590" fill="none" stroke="#cfcfcf" stroke-width="2" stroke-dasharray="6 8"/>
  </svg>
  <div class="svc" style="left:350px;top:220px"><div class="ic"><svg width="34" height="34" viewBox="0 0 24 24" fill="none" stroke="#222" stroke-width="2"><path d="M4 20l8-8M14 4a4 4 0 105 5l-3-1-1-3z"/><path d="M20 20L9 9M4 4l3 1 1 3"/></svg></div>Dent And<br>Deep Protection</div>
  <div class="svc" style="left:670px;top:220px"><div class="ic"><svg width="34" height="34" viewBox="0 0 24 24" fill="none" stroke="#222" stroke-width="2"><path d="M3 16a12 12 0 0118 0z"/><path d="M12 16l4-6"/></svg></div>Windshield<br>Protection</div>
  <div class="svc" style="left:140px;top:380px"><div class="ic"><svg width="34" height="34" viewBox="0 0 24 24" fill="none" stroke="#222" stroke-width="2"><circle cx="12" cy="12" r="9"/><circle cx="12" cy="12" r="3"/></svg></div>Tire &amp; Wheel<br>Protection</div>
  <div class="svc" style="left:880px;top:380px"><div class="ic"><svg width="34" height="34" viewBox="0 0 24 24" fill="none" stroke="#222" stroke-width="2"><path d="M12 3s6 7 6 11a6 6 0 01-12 0c0-4 6-11 6-11z"/></svg></div>Oil<br>Change</div>
  <div class="svc" style="left:40px;top:560px"><div class="ic"><svg width="34" height="34" viewBox="0 0 24 24" fill="none" stroke="#c8141e" stroke-width="2"><circle cx="12" cy="12" r="9"/><path d="M12 7v5l3 2"/></svg></div>24 Hour Roadside<br>Assistance</div>
  <div class="svc" style="left:980px;top:560px"><div class="ic"><svg width="34" height="34" viewBox="0 0 24 24" fill="none" stroke="#222" stroke-width="2"><circle cx="12" cy="9" r="6"/><path d="M8 14l-2 8 6-3 6 3-2-8"/></svg></div>100% Satisfaction</div>
  <div class="hub">
    <div class="badge">24/7</div>
    <h3>24 Hour Roadside Assistance</h3>
    <p>Bluecrest is one of the largest suppliers of auto-related.</p>
  </div>
</section>

<section class="pro">
  <div class="photo" role="img" aria-label="White SUV on a dark studio floor"></div>
  <div class="abs floor"></div>
  <div class="abs tag">Professinal</div>
  <div class="abs big">Car</div>
  <div class="abs big2">Services</div>
  <div class="abs town">In your Town</div>
  <p>Lorem ipsum dolor sit amet consectetur adipiscing elit sed do eiusmod tempor incididunt ut labore et dolore magna aliqua.</p>
  <div class="btn">Book now</div>
</section>

<section class="testimonials">
  <h2>Testimonials</h2>
  <div class="quote" style="left:70px">Sed ut perspiciatis unde omnis iste natus error sit voluptatem accusantium doloremque laudantium, totam rem aperiam eaque ipsa quae ab illo inventore veritatis et quasi architecto beatae vitae dicta sunt explicabo.</div>
  <div class="quote" style="left:430px">Sed ut perspiciatis unde omnis iste natus error sit voluptatem accusantium doloremque laudantium, totam rem aperiam eaque ipsa quae ab illo inventore veritatis et quasi architecto beatae vitae dicta sunt explicabo.</div>
  <div class="quote" style="left:790px">Sed ut perspiciatis unde omnis iste natus error sit voluptatem accusantium doloremque laudantium, totam rem aperiam eaque ipsa quae ab illo inventore veritatis et quasi architecto beatae vitae dicta sunt explicabo.</div>
  <div class="person" style="left:92px"><div class="avatar" role="img" aria-label="Customer portrait"></div>Nora Hallis</div>
  <div class="person" style="left:452px"><div class="avatar" role="img" aria-label="Customer portrait"></div>Peter Lindqvist</div>
  <div class="person" style="left:812px"><div class="avatar" role="img" aria-label="Customer portrait"></div>Nora Hallis</div>
  <div class="arrows">
    <svg width="28" height="16" viewBox="0 0 28 16" fill="none" stroke="#222" stroke-width="2"><path d="M27 8H2M8 2L2 8l6 6"/></svg>
    <svg width="28" height="16" viewBox="0 0 28 16" fill="none" stroke="#222" stroke-width="2"><path d="M1 8h25M20 2l6 6-6 6"/></svg>
  </div>
</section>

<section class="contact">
  <h2>Contact Us</h2>
  <div class="photo car" role="img" aria-label="Red sports car"></div>
  <div class="info" style="top:140px">
    <svg width="20" height="20" viewBox="0 0 24 24" fill="#c8141e"><path d="M6.6 10.8a15 15 0 006.6 6.6l2.2-2.2a1 1 0 011-.25 11.4 11.4 0 003.6.57 1 1 0 011 1V20a1 1 0 01-1 1A17 17 0 013 4a1 1 0 011-1h3.5a1 1 0 011 1c0 1.25.2 2.45.57 3.57a1 1 0 01-.25 1z"/></svg>
    (555) 014-3239</div>
  <div class="info" style="top:200px">
    <svg width="20" height="22" viewBox="0 0 24 24" fill="#c8141e"><path d="M12 2a7 7 0 00-7 7c0 5 7 13 7 13s7-8 7-13a7 7 0 00-7-7zm0 9.5A2.5 2.5 0 1112 6.5a2.5 2.5 0 010 5z"/></svg>
    <span>48 Harbor Lane, Fairhaven<br>NJ 08700</span></div>
  <div class="info" style="top:276px">
    <svg width="20" height="16" viewBox="0 0 24 18" fill="none" stroke="#c8141e" stroke-width="2"><rect x="1" y="1" width="22" height="16"/><path d="M1 1l11 9 11-9"/></svg>
    customerservice@bluecrest.example</div>
  <div class="social"><span></span><span></span><span></span><span></span></div>
  <div class="photo map" role="img" aria-label="Street map showing the garage location"></div>
</section>

<section class="cta">
  <p>If you need any Car related service, don't hesitate to contact us!</p>
  <div class="btn">Make appointment</div>
</section>

<footer class="footer">
  <div class="col" style="left:64px"><h4>About Us</h4><p>Bluecrest one of the largest suppliers of auto-related, supplemental products since 1962, servicing over fifteen million customers annually. Our dedication to excellence is one reason we have the pleasure of working with so many roadside members and providing them with coverage they can trust.</p></div>
  <div class="col" style="left:440px"><h4>Quick Links</h4><ul><li>Home</li><li>About Us</li><li>Services</li><li>Contact Us</li><li>Privacy Policy</li></ul></div>
  <div class="col" style="left:660px"><h4>Our Services</h4><ul><li>Brakes &amp; Brake Repair</li><li>Tire Maintenance</li><li>Shop for Tires</li><li>Steering &amp; Suspension</li><li>Car A/C &amp; Heating Repair</li></ul></div>
  <div class="col" style="left:920px"><h4>Useful Information</h4><ul><li>Wheel Repair</li><li>Emission</li><li>About</li><li>Warranty</li></ul></div>
</footer>

</body>
</html>
```